Bluepeak Comfort HVAC Card

Sale, Install, Maintenance Commercial Vent Hood, Ice Machine & Refrigeration
Air Conditioning Heating & Cooling

Industry/Entity Type

Air Conditioning

Contact Information for Business Card

Bluepeak Comfort
2437 Marisol Ave.
Del Rio Tx, 78852
Ph. (830) 555-0172 Tomas J. Villareal Owner
Ph. (830) 555-0438 Hugo Espinoza Tec.
E-mail. bluepeakcomfort2437@mailnest.example

```html
<!DOCTYPE html>
<html lang="en">
<head>
<meta charset="utf-8">
<title>Bluepeak Comfort – Business Card</title>
<link href="https://fonts.googleapis.com/css2?family=Alegreya:wght@400;700&display=swap" rel="stylesheet">
<style>
  :root {
    --page-bg: #e9e6e1;
    --card-black: #0b0b0c;
    --card-glow: #1f1e20;
    --ink-white: #f4f4f4;
    --ink-grey: #b9b4b1;
    --brand-grey: #9c9592;
    --accent-blue: #2a7fc6;
    --edge: #2b2b2d;
  }
  * { box-sizing: border-box; margin: 0; padding: 0; }
  html, body {
    width: 1200px; height: 900px; overflow: hidden;
    background: var(--page-bg);
    font-family: "Alegreya", Georgia, serif;
  }
  .canvas {
    position: relative; width: 1200px; height: 900px;
    display: flex; flex-direction: column; align-items: center; justify-content: center;
    gap: 50px;
  }
  .card {
    position: relative; width: 600px; height: 343px;
    background: radial-gradient(ellipse at 45% 40%, var(--card-glow) 0%, var(--card-black) 70%);
    border: 1px solid var(--edge);
    box-shadow: 0 10px 24px rgba(0,0,0,.25);
    overflow: hidden;
  }

  /* Front face */
  .card-front .brand {
    position: absolute; left: 0; right: 0; top: 88px;
    display: flex; flex-direction: column; align-items: center; gap: 26px;
    padding-left: 120px;
  }
  .brand-mark {
    width: 64px; height: 64px; background: var(--brand-grey); border-radius: 4px;
  }
  .card-front .brand-name {
    font-size: 34px; letter-spacing: 2px; text-transform: uppercase;
    color: var(--brand-grey); font-weight: 400;
  }

  /* Back face */
  .card-back .brand {
    position: absolute; right: 36px; top: 34px;
    display: flex; flex-direction: column; align-items: flex-end; gap: 12px;
  }
  .card-back .brand-mark {
    width: 40px; height: 40px; background: var(--accent-blue); border-radius: 3px;
    margin-right: 44px;
  }
  .card-back .brand-name {
    font-size: 20px; letter-spacing: 1px; text-transform: uppercase;
    color: var(--ink-grey); font-weight: 400;
  }
  .person { position: absolute; left: 40px; top: 150px; }
  .person-name { font-size: 26px; font-weight: 700; color: var(--ink-white); line-height: 1.1; }
  .person-role { font-size: 18px; color: var(--accent-blue); }
  .contact {
    position: absolute; left: 56px; top: 232px;
    font-size: 16px; line-height: 1.55; color: var(--ink-white);
  }
  .contact .label { color: var(--accent-blue); }
  .contact .note { color: var(--ink-grey); }
</style>
</head>
<body>
  <main class="canvas">
    <section class="card card-front" aria-label="Card front">
      <div class="brand">
        <span class="brand-mark"></span>
        <span class="brand-name">Bluepeak Comfort</span>
      </div>
    </section>

    <section class="card card-back" aria-label="Card back">
      <div class="brand">
        <span class="brand-mark"></span>
        <span class="brand-name">Bluepeak Comfort</span>
      </div>
      <div class="person">
        <p class="person-name">Tomas J. Villareal</p>
        <p class="person-role">Owner</p>
      </div>
      <div class="contact">
        <p>2437 Marisol Ave., Del Rio Tx, 78852</p>
        <p><span class="label">T:</span> (830) 555-0172 &nbsp;<span class="label">M:</span> (830) 555-0438 <span class="note">Hugo Espinoza, Tec.</span></p>
        <p><span class="label">E:</span> bluepeakcomfort2437@mailnest.example</p>
      </div>
    </section>
  </main>
</body>
</html>
```